Book cover for book about Climate Change

Looking for a clean, bold, and attractive cover for a mass-market paperback (5.5"x 8.5") about solving the climate change problem. Title is either "Where the Rivers Begin” or A Garden Left Standing” (your choice), subtitle is "A five-step plan to reverse climate change — to ensure that your grandchildren will live on a clean and comfortable planet," author is Milo Pardrey. Thinking that it *might* feature an image of Earth (or a portion thereof) and its very thin layer of atmosphere -- but STRONGLY encourage other ideas too!

Requirements
Nice to have
• Keep it positive — NOT scary doom-and-gloom

```html
<!DOCTYPE html>
<html lang="en">
<head>
<meta charset="utf-8">
<title>A Garden Left Standing — Book Cover</title>
<link rel="stylesheet" href="https://fonts.googleapis.com/css2?family=Anton&family=Crimson+Text:ital@1&family=Montserrat:wght@600&display=swap">
<style>
  :root {
    --page-bg: #ffffff;
    --space: #000000;
    --title-white: #ffffff;
    --title-blue: #1f4fcc;
    --glow-red: #4a1d18;
    --horizon-light: #c9c2c4;
    --earth-blue: #3e6288;
    --earth-dark: #0d1a24;
  }
  html, body {
    margin: 0;
    width: 1200px;
    height: 1200px;
    overflow: hidden;
    background: var(--page-bg);
  }
  .cover {
    position: absolute;
    left: 238px;
    top: 40px;
    width: 724px;
    height: 1120px;
    background: var(--space);
    overflow: hidden;
    box-shadow: 10px 12px 18px rgba(0,0,0,0.45);
  }
  .cover-art { position: absolute; inset: 0; }
  .subtitle {
    font-family: "Crimson Text", Georgia, serif;
    font-style: italic;
    font-size: 25px;
    fill: var(--title-white);
  }
  .title-text { font-family: "Anton", Impact, sans-serif; }
  .author {
    font-family: "Montserrat", Arial, sans-serif;
    font-weight: 600;
    font-size: 43px;
    letter-spacing: 3.5px;
    fill: var(--title-white);
  }
</style>
</head>
<body>
  <div class="cover">
    <svg class="cover-art" width="724" height="1120" viewBox="0 0 724 1120">
      <defs>
        <linearGradient id="earth-photo-tones" x1="0" y1="0" x2="0" y2="1">
          <stop offset="0" stop-color="var(--space)"/>
          <stop offset="0.3" stop-color="var(--glow-red)"/>
          <stop offset="0.55" stop-color="var(--horizon-light)"/>
          <stop offset="0.75" stop-color="var(--earth-blue)"/>
          <stop offset="1" stop-color="var(--earth-dark)"/>
        </linearGradient>
      </defs>

      <rect class="earth-photo" x="0" y="600" width="724" height="520" fill="url(#earth-photo-tones)" role="img" aria-label="Photograph of Earth's curved horizon seen from space at sunrise, with clouds, oceans and a thin blue atmosphere under a starry sky"/>

      <g class="subtitle">
        <text x="41" y="69" textLength="643" lengthAdjust="spacingAndGlyphs">A five-step plan to reverse climate change to ensure that your</text>
        <text x="59" y="98" textLength="607" lengthAdjust="spacingAndGlyphs">grandchildren will live on a clean and comfortable planet</text>
      </g>

      <g class="title-text">
        <line class="title-rule" x1="35" y1="202" x2="283" y2="202" stroke="var(--title-white)" stroke-width="2"/>
        <line class="title-rule" x1="443" y1="202" x2="684" y2="202" stroke="var(--title-white)" stroke-width="2"/>
        <text x="362" y="243" text-anchor="middle" font-size="90" fill="var(--title-white)">A</text>
        <text x="45" y="429" font-size="176" textLength="639" lengthAdjust="spacingAndGlyphs"><tspan fill="var(--title-blue)">GARDEN</tspan><tspan fill="var(--title-white)"> LEFT</tspan></text>
        <text x="38" y="572" font-size="127" textLength="646" lengthAdjust="spacingAndGlyphs" fill="var(--title-white)">STANDING</text>
      </g>

      <text class="author" x="362" y="1059" text-anchor="middle">MILO PARDREY</text>
    </svg>
  </div>
</body>
</html>
```